Book cover needed for self help business book

Book cover needed and I will provide back cover blurb and barcode to the winning designer. Book may be too small for spine, but I will give you the page number details to confirm. Book information below:

Title: Nine Winters a Trader
Subtitle: Proven Market Methods That Keep Paying Off Now
Author: Maribel Okonte

Design should be clean, modern, and bold—something that appeals to everyday entrepreneurs and resellers. The cover should reflect grit, real-world hustle, and long-term wisdom without looking overly corporate or flashy. I am open to your creative ideas.

I am open to modern designs, but also designs of rugged old covers that simulate a book that may have aged over the years.

I prefer not to have pictures or silhouettes of people

Requirements
Nice to have
• I am open to modern designs, but also designs of rugged old covers that simulate a book that may have aged over the years.
Should not have
• Pictures or silhouettes of people

```html
<!DOCTYPE html>
<html lang="en">
<head>
<meta charset="utf-8">
<title>Nine Winters a Trader — Cover Spread</title>
<link rel="stylesheet" href="https://fonts.googleapis.com/css2?family=Bebas+Neue&family=Montserrat:wght@400;500;600;700&display=swap">
<style>
  :root {
    --paper: #ffffff;
    --ochre: #dc9f4e;
    --ochre-light: #e8c191;
    --charcoal: #343437;
    --teal: #6aaba3;
    --ink: #1e1e20;
    --cream: #f3ead8;
  }
  html, body {
    margin: 0;
    padding: 0;
    width: 1200px;
    height: 857px;
    overflow: hidden;
    background: var(--paper);
  }
  .spread {
    position: absolute;
    left: 25px;
    top: 22px;
    width: 1147px;
    height: 810px;
    background: var(--ochre);
    overflow: hidden;
    font-family: "Montserrat", sans-serif;
    color: var(--ink);
  }
  /* Back cover */
  .back {
    position: absolute;
    left: 0;
    top: 0;
    width: 607px;
    height: 810px;
  }
  .back-title {
    position: absolute;
    left: 0;
    top: 78px;
    width: 596px;
    margin: 0;
    text-align: center;
    font-weight: 700;
    font-size: 36px;
    letter-spacing: -0.5px;
    line-height: 1;
  }
  .back-blurb {
    position: absolute;
    left: 57px;
    top: 141px;
    width: 430px;
    font-size: 12px;
    line-height: 15px;
    text-align: justify;
    font-weight: 500;
  }
  .back-blurb p { margin: 0; }
  .rule {
    position: absolute;
    left: 51px;
    width: 437px;
    height: 1px;
    background: var(--cream);
  }
  .rule-top { top: 419px; }
  .rule-bottom { top: 614px; }
  .author-photo {
    position: absolute;
    left: 51px;
    top: 432px;
    width: 119px;
    height: 164px;
    background: var(--ochre-light);
  }
  .author-bio {
    position: absolute;
    left: 189px;
    top: 436px;
    width: 299px;
    margin: 0;
    font-size: 12px;
    line-height: 15px;
    text-align: justify;
    font-weight: 500;
  }
  /* Spine */
  .spine {
    position: absolute;
    left: 572px;
    top: 0;
    width: 40px;
    height: 810px;
  }
  .spine-text {
    position: absolute;
    left: 40px;
    top: 88px;
    transform-origin: 0 0;
    transform: rotate(90deg);
    white-space: nowrap;
    display: flex;
    align-items: baseline;
    gap: 30px;
  }
  .spine-title {
    font-weight: 700;
    font-size: 30px;
  }
  .spine-author {
    font-weight: 500;
    font-size: 28px;
  }
  /* Front cover */
  .front {
    position: absolute;
    left: 607px;
    top: 0;
    width: 540px;
    height: 810px;
  }
  .front-bands {
    position: absolute;
    inset: 0;
  }
  .front-title {
    position: absolute;
    right: 58px;
    top: 68px;
    margin: 0;
    font-family: "Bebas Neue", sans-serif;
    font-weight: 400;
    font-size: 104px;
    line-height: 0.94;
    color: var(--paper);
    text-align: right;
    letter-spacing: 1px;
  }
  .front-subtitle {
    position: absolute;
    right: 58px;
    top: 353px;
    width: 230px;
    margin: 0;
    font-weight: 600;
    font-size: 21px;
    line-height: 29px;
    text-align: right;
    color: var(--ink);
  }
  .front-author {
    position: absolute;
    right: 45px;
    top: 745px;
    margin: 0;
    font-weight: 600;
    font-size: 40px;
    line-height: 1;
    color: var(--ink);
    white-space: nowrap;
  }
  .price-tag {
    position: absolute;
    left: 48px;
    top: 388px;
  }
</style>
</head>
<body>
<div class="spread">

  <section class="back">
    <h2 class="back-title">NINE WINTERS A TRADER</h2>
    <div class="back-blurb">
      <p>Lorem ipsum dolor sit amet, consectetuer adipiscing elit, sed diam nonummy nibh euismod tincidunt ut laoreet dolore magna aliquam erat volutpat. Ut wisi enim ad minim veniam, quis nostrud exerci tation ullamcorper suscipit lobortis nisl ut aliquip ex ea commodo consequat. Duis autem vel eum iriure dolor in hendrerit in vulputate velit esse molestie consequat, vel illum dolore eu feugiat nulla facilisis at vero eros et accumsan et iusto odio dignissim qui blandit praesent luptatum zzril delenit augue duis dolore te feugait nulla facilisi.</p>
      <p>Lorem ipsum dolor sit amet, cons ectetuer adipiscing elit, sed diam nonummy nibh euismod tincidunt ut laoreet dolore magna aliquam erat volutpat. Ut wisi enim ad minim veniam, quis nostrud exerci tation ullamcorper suscipit lobortis nisl ut aliquip ex ea commodo consequat.</p>
      <p>Lorem ipsum dolor sit amet, consectetuer adipiscing elit, sed diam nonummy nibh euismod tincidunt ut laoreet dolore magna aliquam erat volutpat. Ut wisi enim ad minim veniam, quis nostrud exerci tation ullamcorper suscipit lobortis nisl ut aliquip ex ea commodo consequat. Duis autem vel eum iriure dolor in hendrerit in vulputate</p>
    </div>
    <div class="rule rule-top"></div>
    <div class="author-photo" role="img" aria-label="Author photo placeholder"></div>
    <p class="author-bio">Lorem ipsum dolor sit amet, consectetuer adipiscing elit, sed diam nonummy nibh euismod tincidunt ut laoreet dolore magna aliquam erat volutpat. Ut wisi enim ad minim veniam, quis nostrud exerci tation ullamcorper suscipit lobortis nisl ut aliquip ex ea commodo consequat. Duis autem vel eum iriure dolor in hendrerit in vulputate velit esse molestie consequat, vel illum dolore eu feugiat nulla facilisis at vero eros et accumsan et iusto odio dignissim qui blandit praesent luptatum zzril</p>
    <div class="rule rule-bottom"></div>
  </section>

  <section class="spine">
    <div class="spine-text">
      <span class="spine-title">NINE WINTERS A TRADER</span>
      <span class="spine-author">Maribel Okonte</span>
    </div>
  </section>

  <section class="front">
    <svg class="front-bands" width="540" height="810" viewBox="0 0 540 810" aria-hidden="true">
      <rect x="0" y="0" width="540" height="810" fill="var(--ochre)"/>
      <polygon points="0,0 540,0 540,24 0,593" fill="var(--charcoal)"/>
      <polygon points="40,810 540,272 540,810" fill="var(--teal)"/>
      <line x1="48" y1="810" x2="540" y2="282" stroke="var(--cream)" stroke-width="6" opacity="0.55"/>
      <line x1="0" y1="585" x2="540" y2="18" stroke="var(--ochre)" stroke-width="4" opacity="0.5"/>
    </svg>
    <div class="price-tag" role="img" aria-label="Illustration of a hanging price tag">
      <svg width="116" height="290" viewBox="0 0 116 290" aria-hidden="true">
        <rect x="0" y="85" width="116" height="205" rx="3" fill="var(--charcoal)" opacity="0.35"/>
      </svg>
    </div>
    <h1 class="front-title">NINE WINTERS<br>A TRADER</h1>
    <p class="front-subtitle">Proven Market Methods That Keep Paying Off Now</p>
    <p class="front-author">Maribel Okonte</p>
  </section>

</div>
</body>
</html>
```